Airport Poster

We need a poster, 11" wide by 17" tall that will be hung up in small, private airports around the country. Please see the text for the poster in the attached file.
We can do a full bleed on this poster, and we will be using 4-color printing. Final artwork can be delivered in a PDF. In general, the person reading the poster will be nearby (in other words, the poster does not have to be readable at a distance).
The poster must include our logo (attached).
Imagery can be drawings or photographs.
Overall "feel" should be bright, fun, energized. Typical audience is male, 50+ years of age, high net-worth.
Also... any images of airplanes should be with smaller, single or twin piston airplanes (like a Varnell 318). Please do not use a jet or commercial airliner. THANKS!
Airport

```html
<!DOCTYPE html>
<html lang="en">
<head>
<meta charset="utf-8">
<title>WingBid – Airport Poster</title>
<link rel="stylesheet" href="https://fonts.googleapis.com/css2?family=Alfa+Slab+One&family=Caladea&family=Rammetto+One&display=swap">
<style>
  :root{
    --backdrop:#e8e5de;
    --frame:#ffc800;
    --rule:#ffffff;
    --paper:#fff41f;
    --paper-light:#ffff8a;
    --ink-blue:#1f1fd6;
    --head-blue:#1515ff;
    --red:#ff1010;
    --black:#111111;
    --star:#2ec8f0;
    --sky-top:#3d8fe0;
    --sky-bottom:#bcdcf5;
    --tab-start:#ffb000;
  }
  *{box-sizing:border-box;margin:0;padding:0}
  html,body{width:1000px;height:1200px;overflow:hidden;background:var(--backdrop)}
  .poster{position:absolute;left:112px;top:0;width:776px;height:1200px;background:var(--frame)}
  .poster__sheet{position:absolute;left:32px;top:32px;right:32px;bottom:32px;border:6px solid var(--rule);background:var(--paper);overflow:hidden}
  .poster__inner{position:absolute;left:-38px;top:-38px;width:776px;height:1200px}
  .sweep{position:absolute;left:0;top:0}
  .headline{position:absolute;font-family:"Rammetto One",serif;line-height:1}
  .headline--small{color:var(--head-blue);font-size:30px}
  .headline--looking{left:176px;top:68px}
  .headline--or{left:372px;top:100px;font-size:26px}
  .headline--an{left:190px;top:166px;font-size:26px}
  .box{position:absolute;display:flex;align-items:center;justify-content:center;font-family:"Alfa Slab One",serif;line-height:1}
  .box--buy{left:218px;top:106px;width:146px;height:59px;background:var(--paper);border:6px solid var(--red);color:var(--red);font-size:50px}
  .box--sell{left:364px;top:127px;width:192px;height:59px;background:var(--head-blue);color:#fff;font-size:52px}
  .headline--airplane{left:180px;top:190px;font-family:"Alfa Slab One",serif;font-size:68px;color:var(--red);text-shadow:5px 5px 0 var(--black);letter-spacing:1px}
  .headline--question{left:572px;top:160px;font-family:"Alfa Slab One",serif;font-size:118px;color:var(--red);text-shadow:6px 6px 0 var(--black);transform:rotate(12deg)}
  .benefits{position:absolute;left:76px;top:292px;list-style:none;font-family:"Caladea",serif;font-size:21px;color:var(--ink-blue);line-height:29px}
  .benefits li{position:relative;padding-left:30px}
  .benefits li::before{content:"★";position:absolute;left:0;top:0;color:var(--star);font-size:17px}
  .hero{position:absolute;left:131px;top:432px}
  .section-tab{position:absolute;left:82px;width:250px;height:24px;padding-left:6px;background:linear-gradient(90deg,var(--tab-start),var(--paper) 85%);font-family:"Alfa Slab One",serif;font-size:21px;line-height:24px;color:var(--red)}
  .section-tab--seller{top:663px}
  .section-tab--buyer{top:810px}
  .section-body{position:absolute;left:88px;width:620px;font-family:"Caladea",serif;font-size:15.5px;line-height:29.3px;color:var(--ink-blue)}
  .section-body--seller{top:680px}
  .section-body--buyer{top:827px}
  .brand{position:absolute;left:96px;top:1030px;display:flex;align-items:center;gap:8px;font-family:"Caladea",serif;font-size:26px;font-weight:700;color:#1b3a8c}
  .brand__mark{width:18px;height:18px;background:var(--red)}
  .cta{position:absolute;left:98px;top:1072px;padding:2px 4px;width:560px;background:linear-gradient(90deg,var(--paper-light),var(--paper) 95%);font-family:"Caladea",serif;font-size:18px;color:var(--black)}
  .cta a{color:var(--ink-blue);text-decoration:underline}
  .footer{position:absolute;left:98px;top:1141px;width:251px;border-top:1px solid #9a9a9a;padding-top:3px;font-family:"Caladea",serif;font-size:9px;color:var(--ink-blue);display:flex;justify-content:space-between}
  .footer span:nth-child(2){color:var(--black)}
</style>
</head>
<body>
<main class="poster">
  <div class="poster__sheet">
    <div class="poster__inner">
      <svg class="sweep" width="776" height="1200" viewBox="0 0 776 1200" aria-hidden="true">
        <path d="M38 215 C300 330 560 600 738 1010 L738 1090 C560 650 300 370 38 250 Z" fill="var(--paper-light)" opacity="0.8"/>
      </svg>

      <span class="headline headline--small headline--looking">Looking to</span>
      <span class="headline headline--small headline--or">or</span>
      <div class="box box--buy">BUY</div>
      <div class="box box--sell">SELL</div>
      <span class="headline headline--small headline--an">an</span>
      <span class="headline headline--airplane">AIRPLANE</span>
      <span class="headline headline--question">?</span>

      <ul class="benefits">
        <li>A new website for general aviation aircraft : WingBid.com</li>
        <li>Sellers attract buyers quickly from anywhere in the nation</li>
        <li>Buyers place online bids to win the airplane of your dreams</li>
        <li>Everyone gets Fair, market driven pricing</li>
      </ul>

      <svg class="hero" width="515" height="232" viewBox="0 0 515 232" role="img" aria-label="Photo of a small single-engine piston airplane, like a Varnell 318, flying against a blue sky with white clouds">
        <defs>
          <linearGradient id="sky" x1="0" y1="0" x2="0" y2="1">
            <stop offset="0" stop-color="var(--sky-top)"/>
            <stop offset="1" stop-color="var(--sky-bottom)"/>
          </linearGradient>
          <linearGradient id="plane" x1="0" y1="0" x2="1" y2="0">
            <stop offset="0" stop-color="#f4f4f2" stop-opacity="0"/>
            <stop offset="0.3" stop-color="#f4f4f2" stop-opacity="0.85"/>
            <stop offset="1" stop-color="#f4f4f2" stop-opacity="0.6"/>
          </linearGradient>
        </defs>
        <rect x="206" y="0" width="309" height="232" fill="url(#sky)"/>
        <rect x="0" y="28" width="420" height="135" rx="60" fill="url(#plane)"/>
      </svg>

      <div class="section-tab section-tab--seller">As a seller</div>
      <p class="section-body section-body--seller">you want to make sure your airplane sells quickly and for top dollar. By using<br>WingBid, you’ll reach a broad, nationwide audience of potential buyers who<br>are ready to place immediate offers online. Our bidding system lets multiple buyers<br>compete for your airplane, while your reserve price protects your investment.</p>

      <div class="section-tab section-tab--buyer">As a Buyer</div>
      <p class="section-body section-body--buyer">you want to know all the details about the airplane you’re about to<br>purchase, and you don’t want to pay more than market value. WingBid lets you<br>review full details like logbooks, 337s, and even a mechanic’s survey. Then, our<br>online bidding system lets multiple buyers submit real offers, driving the price to<br>what the market will bear.</p>

      <div class="brand"><span class="brand__mark"></span>WingBid</div>

      <p class="cta">Visit <a href="#">www.wingbid.com</a> today to buy or sell your next airplane!</p>

      <div class="footer"><span>www.wingbid.com</span><span>(555) 014-2290</span><span>hello@wingbid.com</span></div>
    </div>
  </div>
</main>
</body>
</html>
```